Flyer Vacation Gift Certificate

I need to create a beautiful flyer 8.5 x 11 PDF format flyer design. <br/><br/>Instructions:<br/>The flyer will really be a gift voucher for a las vegas vacation getaway. So must have a Las Vegas Theme exciting fun<br/><br/>The voucher should have two modules that will be editable. <br/>Must have a "Compliments Of" area and also must have an "Exclusively For" area<br/><br/>Keep in mind that this flyer will be printed so keep that in mind :)<br/><br/>Here the is the content for the vacation voucher:<br/><br/>There is no doubt that Las Vegas is one of the hottest travel destinations around the world. In fact, some people would even go as far as<br/>saying that perhaps it is THE hottest place to visit. Enjoy up to 4 nights of resort/casino accommodations in exciting Las Vegas, NV. Millions of people travel to this exciting city each year to enjoy its thrills. Thanks to the business you received this certificate from, now you can enjoy exciting Las Vegas, NV too!<br/><br/>Features:<br/>*Travel 7 Days A Week<br/>*Stay Your Choice Of Nights (1-4 Nights)<br/>*Good For Two Adults & Two Children<br/>*Pay Just The Taxes & Fees<br/>*Multiple Travel Date Requests Allowed<br/>*Fully Transferable To Another Person<br/>*Just A 30 Days Advance Notice Required<br/>*You Will Have 12 Months To Complete Travel After Redemption<br/><br/>HOW CAN WE DO THIS?<br/><br/>We contract with the world leading hotel chains and resorts to help them fill their otherwise empty rooms.<br/><br/>We help fill empty rooms which the hotels, resorts and cruise lines turn into additional revenue from other areas of their property and future bookings.<br/><br/>Hotels rarely experience full occupancy, yet they remain open, providing rooms and services at fixed costs. So when hotels give out their rooms by partnering with marketing companies like us, they might miss out on the room fee, but they already didn't have that in the first place, at least now they have the opportunity to gain a customer for their in-house restaurants, room service, their casinos, an extra day stay, future bookings, etc.<br/><br/>VIEW ALL THE DETAILS OF THIS SPECIAL OFFER AND REDEEM ONLINE AT <br/>WWW.TOQUAMERIDIAN.EXAMPLE<br/><br/>Certificate ID # 47261-38014<br/>Expires 02/29/2020<br/><br/><br/>*terms and conditions apply see website for details<br/><br/>KEEP IN MIND THE EXAMPLES I AM UPLOADING ARE SIMPLY TO SHOW YOU THAT THEY CONTAIN THE "COMPLIMENTS OF" AND "EXCLUSIVELY FOR" ELEMENTS. THESE MUST BE INCLUDED IN NEW DESIGN. PLEASE ONLY USE THE CONTENT I PROVIDED IN BRIEF, DONT USE CONTENT FROM EXAMPLES.

Target Market(s)

CONSUMERS THAT HAVE BEEN REWARDED WITH A VACATION CERTIFICATE FOR DOING BUSINESS WITH A COMPANY.

COMPANIES USE THESE AS MARKETING INCENTIVES TO ATTRACT MORE CUSTOMERS AND TO REWARD LOYALTY, ETC.

Industry/Entity Type

Travel Industry

Colors

Designer to choose colors to be used in the design.

Requirements
Must have
• I need to create a beautiful flyer 8.5 x 11 PDF format flyer design.
• Instructions:
• The flyer will really be a gift voucher for a las vegas vacation getaway. So must have a Las Vegas Theme exciting fun
• The voucher should have two modules that will be editable.
• Must have a "Compliments Of" area and also must have an "Exclusively For" area
• Keep in mind that this flyer will be printed so keep that in mind :)
• Here the is the content for the vacation voucher:
• There is no doubt that Las Vegas is one of the hottest travel destinations around the world. In fact, some people would even go as far as
• saying that perhaps it is THE hottest place to visit. Enjoy up to 4 nights of resort/casino accommodations in exciting Las Vegas, NV. Millions of people travel to this exciting city each year to enjoy its thrills. Thanks to the business you received this certificate from, now you can enjoy exciting Las Vegas, NV too!
• Features:
• *Travel 7 Days A Week
• *Stay Your Choice Of Nights (1-4 Nights)
• *Good For Two Adults & Two Children
• *Pay Just The Taxes & Fees
• *Multiple Travel Date Requests Allowed
• *Fully Transferable To Another Person
• *Just A 30 Days Advance Notice Required
• *You Will Have 12 Months To Complete Travel After Redemption
• HOW CAN WE DO THIS?
• We contract with the world leading hotel chains and resorts to help them fill their otherwise empty rooms.
• We help fill empty rooms which the hotels, resorts and cruise lines turn into additional revenue from other areas of their property and future bookings.
• Hotels rarely experience full occupancy, yet they remain open, providing rooms and services at fixed costs. So when hotels give out their rooms by partnering with marketing companies like us, they might miss out on the room fee, but they already didn't have that in the first place, at least now they have the opportunity to gain a customer for their in-house restaurants, room service, their casinos, an extra day stay, future bookings, etc.
• VIEW ALL THE DETAILS OF THIS SPECIAL OFFER AND REDEEM ONLINE AT
• WWW.TOQUAMERIDIAN.EXAMPLE
• Certificate ID # 47261-38014
• Expires 02/29/2020
• *terms and conditions apply see website for details
• KEEP IN MIND THE EXAMPLES I AM UPLOADING ARE SIMPLY TO SHOW YOU THAT THEY CONTAIN THE "COMPLIMENTS OF" AND "EXCLUSIVELY FOR" ELEMENTS. THESE MUST BE INCLUDED IN NEW DESIGN. PLEASE ONLY USE THE CONTENT I PROVIDED IN BRIEF, DONT USE CONTENT FROM EXAMPLES.
Nice to have
• EXCITING LAS VEGAS IMAGES THAT MAKE SOMEONE WANT TO GO THERE

```html
<!DOCTYPE html>
<html lang="en">
<head>
<meta charset="utf-8">
<title>Las Vegas Vacation Gift Certificate</title>
<link rel="stylesheet" href="https://fonts.googleapis.com/css2?family=Lato:ital,wght@0,400;0,700;0,900;1,400;1,700&display=swap">
<style>
  :root {
    --page-bg: #6b6b6b;
    --paper: #ffffff;
    --ink: #1d1d1d;
    --brand-blue: #0d5e8c;
    --brand-navy: #0b416e;
    --brand-gold: #dcd6a6;
    --teal: #2f7f8a;
    --field: #f3f3f3;
    --photo-sky: #9cc7cf;
    --photo-green: #4f7a3c;
    --photo-roof: #c98e7b;
  }
  * { box-sizing: border-box; margin: 0; padding: 0; }
  html, body { width: 1200px; height: 1200px; overflow: hidden; background: var(--page-bg); }
  body { font-family: "Lato", sans-serif; color: var(--ink); position: relative; }

  .flyer {
    position: absolute; left: 141px; top: 10px;
    width: 1019px; height: 1310px;
    background: var(--paper);
    transform: scale(0.9); transform-origin: 0 0;
    overflow: hidden;
  }
  .hero { position: absolute; left: 0; top: 0; width: 1019px; height: 520px; }

  .intro-rule { position: absolute; left: 32px; top: 268px; width: 140px; height: 5px; background: var(--brand-blue); }
  .intro-lead {
    position: absolute; left: 32px; top: 284px; width: 520px;
    font-style: italic; font-weight: 400; font-size: 27px; line-height: 31px; letter-spacing: -0.4px;
  }
  .intro-body {
    position: absolute; left: 32px; top: 425px; width: 600px;
    font-size: 16px; line-height: 19.5px; letter-spacing: -0.2px;
  }

  .ribbon { position: absolute; display: flex; align-items: center; justify-content: center; }
  .ribbon svg { position: absolute; inset: 0; }
  .ribbon span { position: relative; color: #fff; font-weight: 700; letter-spacing: 0.5px; }
  .ribbon-features { left: 379px; top: 548px; width: 257px; height: 49px; }
  .ribbon-features span { font-size: 30px; }
  .ribbon-how { left: 272px; top: 751px; width: 474px; height: 49px; }
  .ribbon-how span { font-size: 30px; }

  .feature-col { position: absolute; top: 620px; list-style: none; font-size: 16.5px; line-height: 29px; }
  .feature-col li, .how-list li { position: relative; padding-left: 18px; }
  .feature-col li::before, .how-list li::before {
    content: ""; position: absolute; left: 0; width: 9px; height: 9px; border-radius: 50%; background: var(--brand-blue);
  }
  .feature-col li::before { top: 10px; }
  .feature-col li.nobullet::before { display: none; }
  .col-a { left: 32px; }
  .col-b { left: 360px; }
  .col-c { left: 685px; width: 320px; }

  .how-list { position: absolute; left: 32px; top: 824px; width: 962px; list-style: none; font-size: 16px; line-height: 20.5px; letter-spacing: -0.2px; }
  .how-list li { margin-bottom: 8px; }
  .how-list li::before { top: 6px; }

  .module-title {
    position: absolute; top: 1006px; width: 472px; text-align: center;
    color: var(--brand-blue); font-weight: 900; font-size: 24px; letter-spacing: 0.5px;
  }
  .module-box { position: absolute; top: 1052px; height: 151px; background: var(--field); border-radius: 12px; }
  .compliments { left: 30px; }
  .exclusive { left: 515px; }
  .module-box.compliments, .module-box.exclusive { width: 472px; }

  .cert-id { position: absolute; left: 38px; top: 1221px; font-size: 20px; font-weight: 700; }
  .terms { position: absolute; left: 390px; top: 1226px; font-size: 13px; }
  .expires { position: absolute; right: 38px; top: 1221px; font-size: 20px; font-weight: 700; }

  .redeem-band {
    position: absolute; left: 0; top: 1252px; width: 1019px; height: 58px;
    background: linear-gradient(90deg, var(--brand-gold) 0%, var(--brand-blue) 28%, var(--brand-navy) 55%, var(--brand-blue) 80%, var(--brand-gold) 100%);
    color: #fff; font-weight: 700; font-size: 17px; letter-spacing: 0.2px;
    display: flex; align-items: center; justify-content: center;
  }
</style>
</head>
<body>
<main class="flyer">
  <svg class="hero" viewBox="0 0 1019 520" aria-hidden="false">
    <defs>
      <linearGradient id="photoTone" x1="0" y1="0" x2="0.4" y2="1">
        <stop offset="0" stop-color="#a9cfd4"/>
        <stop offset="0.3" stop-color="#6f9b6b"/>
        <stop offset="0.65" stop-color="#4f7a3c"/>
        <stop offset="1" stop-color="#8a8f6e"/>
      </linearGradient>
      <linearGradient id="stripTone" x1="0" y1="0" x2="0" y2="1">
        <stop offset="0" stop-color="#3e5a9e"/>
        <stop offset="1" stop-color="#a74a7a"/>
      </linearGradient>
      <linearGradient id="signTone" x1="0" y1="0" x2="0" y2="1">
        <stop offset="0" stop-color="#2f5f9e"/>
        <stop offset="1" stop-color="#d8a36a"/>
      </linearGradient>
    </defs>
    <path role="img" aria-label="Aerial photo of a Las Vegas resort with lake, gardens and terracotta roofs"
          d="M0 0 H1019 V420 C900 400 820 390 760 380 C560 300 300 220 0 235 Z" fill="url(#photoTone)"/>
    <path d="M0 0 H1019 V0 C700 60 400 70 0 90 Z" fill="#fff" opacity="0"/>
    <path d="M0 80 C150 20 300 0 420 0" stroke="#fff" stroke-width="6" fill="none"/>
    <path d="M0 140 C250 70 500 100 800 20 L900 0" stroke="#fff" stroke-width="10" fill="none"/>
    <path d="M0 200 C300 90 600 150 1000 10" stroke="#fff" stroke-width="5" fill="none"/>
    <path d="M330 0 C480 60 700 70 1019 0 V0 Z" fill="#fff"/>
    <path d="M0 235 C300 220 560 300 760 380 C820 390 900 400 1019 420 V520 H0 Z" fill="#fff"/>
    <circle cx="709" cy="417" r="87" fill="#fff"/>
    <circle cx="709" cy="417" r="84" fill="var(--brand-blue)"/>
    <circle role="img" aria-label="Photo of the Las Vegas Strip lit up at dusk" cx="709" cy="417" r="78" fill="url(#stripTone)"/>
    <circle cx="899" cy="417" r="87" fill="#fff"/>
    <circle cx="899" cy="417" r="84" fill="var(--brand-blue)"/>
    <circle role="img" aria-label="Photo of the Las Vegas welcome sign with palm trees" cx="899" cy="417" r="78" fill="url(#signTone)"/>
  </svg>

  <div class="intro-rule"></div>
  <p class="intro-lead">There is no doubt that Las Vegas is one of the hottest travel destinations around the world. In fact, some people would even go as far as</p>
  <p class="intro-body">saying that perhaps it is THE hottest place to visit. Enjoy up to 4 nights of resort/casino accommodations in exciting Las Vegas, NV. Millions of people travel to this exciting city each year to enjoy its thrills. Thanks to the business you received this certificate from, now you can enjoy exciting Las Vegas, NV too!</p>

  <div class="ribbon ribbon-features">
    <svg viewBox="0 0 257 49" preserveAspectRatio="none">
      <defs>
        <linearGradient id="ribbonA" x1="0" x2="1">
          <stop offset="0" stop-color="#dcd6a6"/><stop offset="0.45" stop-color="#0d5e8c"/><stop offset="1" stop-color="#dcd6a6"/>
        </linearGradient>
      </defs>
      <polygon points="0,0 257,0 240,24.5 257,49 0,49 17,24.5" fill="url(#ribbonA)"/>
    </svg>
    <span>FEATURES:</span>
  </div>

  <ul class="feature-col col-a">
    <li>Travel 7 Days A Week</li>
    <li>Stay Your Choice Of Nights (1-4 Nights)</li>
    <li>Good For Two Adults &amp; Two Children</li>
  </ul>
  <ul class="feature-col col-b">
    <li>Pay Just The Taxes &amp; Fees</li>
    <li>Multiple Travel Date Requests Allowed</li>
    <li>Fully Transferable To Another Person</li>
  </ul>
  <ul class="feature-col col-c">
    <li>Just A 30 Days Advance Notice Required</li>
    <li>You Will Have 12 Months To Complete Travel After Redemption</li>
  </ul>

  <div class="ribbon ribbon-how">
    <svg viewBox="0 0 474 49" preserveAspectRatio="none">
      <defs>
        <linearGradient id="ribbonB" x1="0" x2="1">
          <stop offset="0" stop-color="#dcd6a6"/><stop offset="0.45" stop-color="#0d5e8c"/><stop offset="1" stop-color="#dcd6a6"/>
        </linearGradient>
      </defs>
      <polygon points="0,0 474,0 457,24.5 474,49 0,49 17,24.5" fill="url(#ribbonB)"/>
    </svg>
    <span>HOW CAN WE DO THIS?</span>
  </div>

  <ul class="how-list">
    <li>We contract with the world leading hotel chains and resorts to help them fill their otherwise empty rooms.</li>
    <li>We help fill empty rooms which the hotels, resorts and cruise lines turn into additional revenue from other areas of their property and future bookings.</li>
    <li>Hotels rarely experience full occupancy, yet they remain open, providing rooms and services at fixed costs. So when hotels give out their rooms by partnering with marketing companies like us, they might miss out on the room fee, but they already didn't have that in the first place, at least now they have the opportunity to gain a customer for their in-house restaurants, room service, their casinos, an extra day stay, future bookings, etc.</li>
  </ul>

  <h2 class="module-title" style="left:30px">COMPLIMENTS OF</h2>
  <h2 class="module-title" style="left:540px">EXCLUSIVELY FOR</h2>
  <div class="module-box compliments"></div>
  <div class="module-box exclusive"></div>

  <p class="cert-id">Certificate ID # 47261-38014</p>
  <p class="terms">*terms and conditions apply see website for details</p>
  <p class="expires">Expires 02/29/2020</p>

  <div class="redeem-band">VIEW ALL THE DETAILS OF THIS SPECIAL OFFER AND REDEEM ONLINE AT&nbsp; WWW.TOQUAMERIDIAN.EXAMPLE</div>
</main>
</body>
</html>
```